Business Card Design Project

Cyber Security. Company name is quietBastion.

Industry/Entity Type

Computer Security

Contact Information for Business Card

Gordon Vastrick
Founder and Chief Hacker

2184 W. Harlow Ave.
Suite 314
Chicago, IL 60689
773.555.0193
gordon.vastrick@quietbastion.example
www.quietbastion.example

```html
<!DOCTYPE html>
<html lang="en">
<head>
<meta charset="utf-8">
<title>quietBastion business card</title>
<link rel="stylesheet" href="https://fonts.googleapis.com/css2?family=Open+Sans:wght@400;600&family=Roboto:ital,wght@0,500;0,700;1,500&display=swap">
<style>
  :root {
    --page: #e4e6e8;
    --front: #323746;
    --back: #6079c0;
    --back-mark: #7389c9;
    --white: #ffffff;
    --ink-dark: #2f3444;
    --stripe-orange: #e8632a;
    --stripe-sand: #bcae9a;
    --stripe-green: #7dba3f;
    --accent-dot: #e8632a;
  }
  * { margin: 0; padding: 0; box-sizing: border-box; }
  html, body {
    width: 1200px; height: 1197px; overflow: hidden;
    background: var(--page);
  }
  .card {
    position: absolute; left: 226px; width: 724px; height: 413px;
  }
  .card-front { top: 90px; background: var(--front); }
  .card-back { top: 655px; background: var(--back); }

  .brand {
    position: absolute; left: 0; right: 0; top: 232px;
    display: flex; align-items: center; justify-content: center; gap: 18px;
  }
  .brand-dot {
    width: 44px; height: 44px; border-radius: 50%; background: var(--accent-dot);
  }
  .brand-name {
    font-family: "Open Sans", sans-serif; font-weight: 400;
    font-size: 64px; line-height: 1; color: var(--white); letter-spacing: -0.5px;
  }

  .stripes { position: absolute; top: 350px; width: 192px; }
  .stripes-left { left: 0; }
  .stripes-right { right: 0; }
  .stripe { height: 5px; margin-bottom: 11px; }
  .stripe-orange { background: var(--stripe-orange); }
  .stripe-sand { background: var(--stripe-sand); }
  .stripe-green { background: var(--stripe-green); }
  .website {
    position: absolute; left: 192px; right: 192px; top: 352px;
    text-align: center; font-family: "Open Sans", sans-serif; font-weight: 400;
    font-size: 26px; color: var(--white); letter-spacing: 0.5px;
  }

  .back-mark {
    position: absolute; left: 87px; top: 111px;
    width: 176px; height: 176px; border-radius: 50%; background: var(--back-mark);
  }
  .person {
    position: absolute; right: 43px; top: 50px; text-align: right;
    font-family: "Roboto", sans-serif;
  }
  .person-name { font-weight: 700; font-size: 32px; color: var(--white); }
  .person-title {
    font-weight: 500; font-style: italic; font-size: 15px;
    color: var(--ink-dark); margin-top: 4px;
  }
  .contacts {
    position: absolute; left: 346px; top: 194px; list-style: none;
    font-family: "Roboto", sans-serif; font-weight: 500; font-size: 16px;
    color: var(--white); line-height: 20px;
  }
  .contact { display: flex; align-items: flex-start; margin-bottom: 24px; }
  .contact-icon { width: 20px; height: 20px; margin-right: 33px; flex: none; }
</style>
</head>
<body>
  <section class="card card-front">
    <div class="brand">
      <span class="brand-dot"></span>
      <span class="brand-name">quietBastion</span>
    </div>
    <div class="stripes stripes-left">
      <div class="stripe stripe-orange"></div>
      <div class="stripe stripe-sand"></div>
      <div class="stripe stripe-green"></div>
    </div>
    <div class="website">www.quietbastion.example</div>
    <div class="stripes stripes-right">
      <div class="stripe stripe-orange"></div>
      <div class="stripe stripe-sand"></div>
      <div class="stripe stripe-green"></div>
    </div>
  </section>

  <section class="card card-back">
    <div class="back-mark"></div>
    <div class="person">
      <div class="person-name">Gordon Vastrick</div>
      <div class="person-title">Founder and Chief Hacker</div>
    </div>
    <ul class="contacts">
      <li class="contact">
        <svg class="contact-icon" viewBox="0 0 20 20" aria-hidden="true">
          <rect x="5" y="1" width="10" height="18" rx="2" fill="none" stroke="#2f3444" stroke-width="2"/>
          <line x1="8" y1="15.5" x2="12" y2="15.5" stroke="#2f3444" stroke-width="1.5"/>
        </svg>
        <span>773.555.0193</span>
      </li>
      <li class="contact">
        <svg class="contact-icon" viewBox="0 0 20 20" aria-hidden="true">
          <rect x="2" y="5" width="16" height="11" fill="none" stroke="#2f3444" stroke-width="1.5"/>
          <polyline points="2,5 10,11 18,5" fill="none" stroke="#2f3444" stroke-width="1.5"/>
        </svg>
        <span>gordon.vastrick@quietbastion.example</span>
      </li>
      <li class="contact">
        <svg class="contact-icon" viewBox="0 0 20 20" aria-hidden="true">
          <path d="M10 1a6 6 0 0 0-6 6c0 4.5 6 12 6 12s6-7.5 6-12a6 6 0 0 0-6-6z" fill="#2f3444"/>
          <circle cx="10" cy="7" r="2.2" fill="#6079c0"/>
        </svg>
        <span>2184 W. Harlow Ave.<br>Suite 314<br>Chicago, IL 60689</span>
      </li>
    </ul>
  </section>
</body>
</html>
```